A 'new law' boutique Australian law firm that provides specialist employment law and people managem

We value helping clients create results with respect workplaces. What differentiates us is we provide actionable training in understanding and dealing with people and ensure legal compliance fits with this approach. We would like a fresh approach to our training overview documents that we currently use in our current law firm (6 attached). Please use pictures, symbols etc consistent with our non-traditional law approach that captures the approach of each training session.. Attached is the logo and draft letterhead for Brindle Legal which will launch soon.

Target Market(s)

HR Managers and in-house lawyers (non employment specialists) in mid-large Australian companies that are progressive with a relationship based approach to managing employee behaviours and disputes.

Industry/Entity Type

Human Resource

Font styles to use
Sans Serif

Colors
3176b5
33a6d7

Requirements
Must have
• 1 or 2 page PDF for each of the 6 documents that the wording supplied goes into your design which will be pretty similar as we want consistency with our documents

```html
<!DOCTYPE html>
<html lang="en">
<head>
<meta charset="utf-8">
<title>Brindle Legal – Training Overview Flyers</title>
<link href="https://fonts.googleapis.com/css2?family=Open+Sans:wght@300;400;600;700&family=Roboto+Condensed:wght@300;400;700&display=swap" rel="stylesheet">
<style>
:root{
  --stage:#8b8e92;
  --blue:#3176b5;
  --blue-dark:#1d5c9e;
  --blue-light:#33a6d7;
  --ink:#5d6166;
  --rule:#c7d4e4;
  --footer:#4d6d95;
  --white:#ffffff;
}
*{box-sizing:border-box;margin:0;padding:0}
html,body{width:871px;height:1200px;overflow:hidden}
body{background:var(--stage);font-family:"Open Sans",Arial,sans-serif;position:relative}

.masthead{position:absolute;top:82px;left:0;width:871px;text-align:center;
  font-weight:700;font-size:40px;color:#404244;letter-spacing:.5px}

.flyer-label{position:absolute;width:293px;text-align:center;color:var(--white);
  font-size:22px;font-weight:400;letter-spacing:.5px}

.flyer{position:absolute;width:293px;height:412px;background:var(--white);overflow:hidden}

.hero{position:absolute;left:0;top:0;width:293px;height:110px}
.hero-photo{position:absolute;top:0;height:100px}
.photo-office{background:linear-gradient(135deg,#d9cfc4,#a99785 55%,#6d5d52)}
.photo-studio{background:linear-gradient(180deg,#f6f7f8,#e3e7ec)}
.swoosh{position:absolute;left:0;top:0;width:293px;height:110px}
.brand{position:absolute;font-weight:600;font-size:11.5px;color:var(--blue);letter-spacing:.2px}

.need{position:absolute;left:0;top:104px;width:118px;bottom:20px;
  background:linear-gradient(180deg,var(--blue) 0%,var(--blue-dark) 100%);
  color:var(--white);padding:6px 7px 0 7px;display:flex;flex-direction:column;
  font-size:3.7px;line-height:1.32}
.need h3{font-size:5px;font-weight:700;letter-spacing:.2px;margin:3px 0 2px}
.need h5{font-size:4.4px;font-weight:700;margin:3px 0 1.5px}
.need p{margin-bottom:2.5px}
.need .lead{font-weight:700;font-size:4px}
.need ol{padding-left:6px;margin-top:1px}
.need li{margin-bottom:1.5px}
.side-photo{margin:auto -7px 0;height:92px;background:linear-gradient(180deg,#b7c9dc,#e9eef3 70%,#ccd6e0)}

.main{position:absolute;left:124px;right:7px;top:108px;bottom:24px;display:flex;flex-direction:column}
.title{font-family:"Roboto Condensed",Arial,sans-serif;line-height:.98;margin:6px 0 8px}
.title .lead-line{display:block;color:var(--blue);font-weight:400}
.title .tail-line{display:block;color:var(--ink);font-weight:300}
.overview-head{font-size:4.4px;font-weight:700;color:var(--blue);letter-spacing:.3px;margin-bottom:3px}
.overview-head span{color:var(--ink);font-weight:400}
.overview{flex:1;display:flex;flex-direction:column;border:0.8px solid var(--rule);background:#f7f9fc}
.topic{flex:1;display:grid;grid-template-columns:66px 1fr;border-top:0.8px solid var(--rule);padding:3px 3px}
.topic:first-child{border-top:none}
.topic-name{color:var(--blue);font-size:3.6px;line-height:1.3;padding-right:4px}
.topic-points{list-style:none;font-size:3.3px;line-height:1.3;color:var(--ink)}
.topic-points li{position:relative;padding-left:4px;margin-bottom:1px}
.topic-points li::before{content:"";position:absolute;left:0;top:1.2px;width:2px;height:2px;border-radius:50%;border:0.5px solid var(--blue-light)}
.strip-photo{height:72px;margin-top:4px;background:linear-gradient(90deg,#c6d2df,#e7ecf1 40%,#d3c7bb)}

.contact{position:absolute;left:0;right:0;bottom:0;height:20px;background:var(--footer);
  color:var(--white);font-size:3.4px;line-height:1.3;display:flex;align-items:center;padding:0 8px 0 124px;gap:10px}
.contact .dot{width:4px;height:4px;border-radius:50%;background:var(--white);display:inline-block;margin-left:2px}
.contact .social{margin-left:auto}
</style>
</head>
<body>

<div class="masthead">Brindle Legal</div>

<div class="flyer-label" style="left:54px;top:174px">FLYER 1</div>
<div class="flyer-label" style="left:533px;top:174px">FLYER 2</div>
<div class="flyer-label" style="left:54px;top:678px">FLYER 3</div>
<div class="flyer-label" style="left:533px;top:678px">FLYER 4</div>

<!-- Flyer 1 -->
<article class="flyer" style="left:54px;top:213px">
  <div class="hero">
    <div class="hero-photo photo-office" style="left:118px;width:175px" role="img" aria-label="Photo of colleagues seated in a row at a workshop"></div>
    <svg class="swoosh" viewBox="0 0 293 110" aria-hidden="true">
      <path d="M0 0H128C122 34 112 52 90 62C60 74 30 68 0 56Z" fill="#ffffff"/>
      <path d="M0 56C60 88 150 100 293 92V102C200 104 150 106 118 110H0Z" fill="#3176b5"/>
      <path d="M0 50C60 82 150 94 293 86" fill="none" stroke="#33a6d7" stroke-width="2"/>
    </svg>
    <div class="brand" style="left:40px;top:44px">Brindle Legal</div>
  </div>
  <aside class="need">
    <h3>TRAINING NEED</h3>
    <p>Workplace conflict often starts small and grows costly when left alone. Clear expectations, early action and respectful conversations help teams stay productive, engaged and safe while reducing legal risk for everyone involved.</p>
    <p>Managers need practical tools to recognise problem behaviour, respond with confidence and keep decisions fair, consistent and well documented across the whole organisation.</p>
    <h5>Traditional Processes Just Aren't Working. They are Usually:</h5>
    <p>Workplace conflict often starts small and grows costly when left alone. Clear expectations, early action and respectful conversations help teams stay productive, engaged and safe while reducing legal risk for everyone involved.</p>
    <h3>LEARNING OUTCOMES</h3>
    <p class="lead">Participants will apply the learnings to understand:</p>
    <ol>
      <li>Understand the legal framework that applies to workplace behaviour.</li>
      <li>Recognise early signs of conflict and act before issues escalate.</li>
      <li>Apply a simple, fair process to complaints and concerns.</li>
      <li>Hold respectful conversations that build trust and accountability.</li>
    </ol>
  </aside>
  <section class="main">
    <h2 class="title"><span class="lead-line" style="font-size:13px">CO-OPERATIVELY COMPLIANT</span><span class="tail-line" style="font-size:23px">WORKPLACES</span></h2>
    <div class="overview-head">OVERVIEW <span>OF</span> TRAINING</div>
    <div class="overview">
      <div class="topic"><div class="topic-name">Social Safety is Basic Biology</div><ul class="topic-points"><li>What it means in practice, why it matters and how to respond well.</li><li>Practical examples, common mistakes and simple steps managers can take.</li></ul></div>
      <div class="topic"><div class="topic-name">Building Effective Relationships: Trust and Respect</div><ul class="topic-points"><li>What it means in practice, why it matters and how to respond well.</li><li>Practical examples, common mistakes and simple steps managers can take.</li></ul></div>
      <div class="topic"><div class="topic-name">Ground Rules: Understanding the workplace behaviour legal framework</div><ul class="topic-points"><li>What it means in practice, why it matters and how to respond well.</li><li>Practical examples, common mistakes and simple steps managers can take.</li></ul></div>
      <div class="topic"><div class="topic-name">Guidelines: How to avoid unlawful behaviour and generally be effective in a diverse workplace</div><ul class="topic-points"><li>What it means in practice, why it matters and how to respond well.</li><li>Practical examples, common mistakes and simple steps managers can take.</li></ul></div>
      <div class="topic"><div class="topic-name">Activities</div><ul class="topic-points"><li>What it means in practice, why it matters and how to respond well.</li><li>Practical examples, common mistakes and simple steps managers can take.</li></ul></div>
    </div>
  </section>
  <footer class="contact"><span>12 Harbour Lane, Northgate<br>Level 3, 80 Quay St, Southbank</span><span>1300 555 019</span><span>info@brindlelegal.com.au<br>www.brindlelegal.com.au</span><span class="social"><i class="dot"></i><i class="dot"></i></span></footer>
</article>

<!-- Flyer 2 -->
<article class="flyer" style="left:533px;top:213px">
  <div class="hero">
    <div class="hero-photo photo-office" style="left:0;width:190px" role="img" aria-label="Photo of a presenter standing before a seated group"></div>
    <svg class="swoosh" viewBox="0 0 293 110" aria-hidden="true">
      <path d="M293 0H186C178 30 176 58 200 70C230 82 262 78 293 70Z" fill="#ffffff"/>
      <path d="M0 56C60 88 150 100 293 92V102C200 104 150 106 118 110H0Z" fill="#3176b5"/>
      <path d="M0 50C60 82 150 94 293 86" fill="none" stroke="#33a6d7" stroke-width="2"/>
    </svg>
    <div class="brand" style="left:212px;top:44px">Brindle Legal</div>
  </div>
  <aside class="need">
    <h3>TRAINING NEED</h3>
    <p>Workplace conflict often starts small and grows costly when left alone. Clear expectations, early action and respectful conversations help teams stay productive, engaged and safe while reducing legal risk for everyone involved.</p>
    <p>Managers need practical tools to recognise problem behaviour, respond with confidence and keep decisions fair, consistent and well documented across the whole organisation.</p>
    <h3>LEARNING OUTCOMES</h3>
    <p class="lead">Training will enable participants to perform their role of Contact Officer and to understand:</p>
    <ol>
      <li>Understand the legal framework that applies to workplace behaviour.</li>
      <li>Recognise early signs of conflict and act before issues escalate.</li>
      <li>Apply a simple, fair process to complaints and concerns.</li>
      <li>Hold respectful conversations that build trust and accountability.</li>
    </ol>
    <div class="side-photo" role="img" aria-label="Photo of a smiling group of staff standing together"></div>
  </aside>
  <section class="main">
    <h2 class="title"><span class="lead-line" style="font-size:21px">CONTACT OFFICER</span><span class="tail-line" style="font-size:34px">TRAINING</span></h2>
    <div class="overview-head">OVERVIEW <span>OF</span> TRAINING</div>
    <div class="overview">
      <div class="topic"><div class="topic-name">Discrimination</div><ul class="topic-points"><li>What it means in practice, why it matters and how to respond well.</li><li>Practical examples, common mistakes and simple steps managers can take.</li></ul></div>
      <div class="topic"><div class="topic-name">Harassment</div><ul class="topic-points"><li>What it means in practice, why it matters and how to respond well.</li><li>Practical examples, common mistakes and simple steps managers can take.</li></ul></div>
      <div class="topic"><div class="topic-name">Bullying</div><ul class="topic-points"><li>What it means in practice, why it matters and how to respond well.</li><li>Practical examples, common mistakes and simple steps managers can take.</li></ul></div>
      <div class="topic"><div class="topic-name">Victimisation and Vilification</div><ul class="topic-points"><li>What it means in practice, why it matters and how to respond well.</li><li>Practical examples, common mistakes and simple steps managers can take.</li></ul></div>
      <div class="topic"><div class="topic-name">Adverse Action</div><ul class="topic-points"><li>What it means in practice, why it matters and how to respond well.</li><li>Practical examples, common mistakes and simple steps managers can take.</li></ul></div>
      <div class="topic"><div class="topic-name">The Contact Officer's role</div><ul class="topic-points"><li>What it means in practice, why it matters and how to respond well.</li><li>Practical examples, common mistakes and simple steps managers can take.</li></ul></div>
      <div class="topic"><div class="topic-name">Grievance Options</div><ul class="topic-points"><li>What it means in practice, why it matters and how to respond well.</li><li>Practical examples, common mistakes and simple steps managers can take.</li></ul></div>
      <div class="topic"><div class="topic-name">Test Learning</div><ul class="topic-points"><li>What it means in practice, why it matters and how to respond well.</li><li>Practical examples, common mistakes and simple steps managers can take.</li></ul></div>
    </div>
  </section>
  <footer class="contact"><span>12 Harbour Lane, Northgate<br>Level 3, 80 Quay St, Southbank</span><span>1300 555 019</span><span>info@brindlelegal.com.au<br>www.brindlelegal.com.au</span><span class="social"><i class="dot"></i><i class="dot"></i></span></footer>
</article>

<!-- Flyer 3 -->
<article class="flyer" style="left:54px;top:732px">
  <div class="hero">
    <div class="hero-photo photo-office" style="left:0;width:200px" role="img" aria-label="Photo of colleagues talking around a laptop"></div>
    <svg class="swoosh" viewBox="0 0 293 110" aria-hidden="true">
      <path d="M293 0H196C186 30 184 58 206 70C234 82 262 78 293 70Z" fill="#ffffff"/>
      <path d="M0 56C60 88 150 100 293 92V102C200 104 150 106 118 110H0Z" fill="#3176b5"/>
      <path d="M0 50C60 82 150 94 293 86" fill="none" stroke="#33a6d7" stroke-width="2"/>
    </svg>
    <div class="brand" style="left:218px;top:40px">Brindle Legal</div>
  </div>
  <aside class="need">
    <h3>TRAINING NEED</h3>
    <p>Workplace conflict often starts small and grows costly when left alone. Clear expectations, early action and respectful conversations help teams stay productive, engaged and safe while reducing legal risk for everyone involved.</p>
    <p>Managers need practical tools to recognise problem behaviour, respond with confidence and keep decisions fair, consistent and well documented across the whole organisation.</p>
    <h3>LEARNING OUTCOMES</h3>
    <p class="lead">Participants will practice and apply the learnings to:</p>
    <ol>
      <li>Understand the legal framework that applies to workplace behaviour.</li>
      <li>Recognise early signs of conflict and act before issues escalate.</li>
      <li>Apply a simple, fair process to complaints and concerns.</li>
      <li>Hold respectful conversations that build trust and accountability.</li>
    </ol>
    <div class="side-photo" role="img" aria-label="Photo of a professional woman with colleagues behind her"></div>
  </aside>
  <section class="main">
    <h2 class="title"><span class="lead-line" style="font-size:35px;font-weight:700">EFFECTIVE</span><span class="tail-line" style="font-size:17px">COMMUNICATION</span></h2>
    <div class="overview-head">OVERVIEW <span>OF</span> TRAINING</div>
    <div class="overview">
      <div class="topic"><div class="topic-name">Understanding what is and isn't effective communication</div><ul class="topic-points"><li>What it means in practice, why it matters and how to respond well.</li><li>Practical examples, common mistakes and simple steps managers can take.</li></ul></div>
      <div class="topic"><div class="topic-name">Applying DISC to the Workplace</div><ul class="topic-points"><li>What it means in practice, why it matters and how to respond well.</li><li>Practical examples, common mistakes and simple steps managers can take.</li></ul></div>
      <div class="topic"><div class="topic-name">Advanced DISC style Interpretation</div><ul class="topic-points"><li>What it means in practice, why it matters and how to respond well.</li><li>Practical examples, common mistakes and simple steps managers can take.</li></ul></div>
      <div class="topic"><div class="topic-name">Activities</div><ul class="topic-points"><li>What it means in practice, why it matters and how to respond well.</li><li>Practical examples, common mistakes and simple steps managers can take.</li></ul></div>
    </div>
    <div class="strip-photo" role="img" aria-label="Photo of a team holding up coloured speech bubbles"></div>
  </section>
  <footer class="contact"><span>12 Harbour Lane, Northgate<br>Level 3, 80 Quay St, Southbank</span><span>1300 555 019</span><span>info@brindlelegal.com.au<br>www.brindlelegal.com.au</span><span class="social"><i class="dot"></i><i class="dot"></i></span></footer>
</article>

<!-- Flyer 4 -->
<article class="flyer" style="left:533px;top:732px">
  <div class="hero">
    <div class="hero-photo photo-studio" style="left:0;width:293px" role="img" aria-label="Photo of business people standing on steps against a white backdrop"></div>
    <svg class="swoosh" viewBox="0 0 293 110" aria-hidden="true">
      <path d="M0 56C60 88 150 100 293 92V102C200 104 150 106 118 110H0Z" fill="#3176b5"/>
      <path d="M0 50C60 82 150 94 293 86" fill="none" stroke="#33a6d7" stroke-width="2"/>
    </svg>
    <div class="brand" style="left:210px;top:48px">Brindle Legal</div>
  </div>
  <aside class="need">
    <h3>TRAINING NEED</h3>
    <p>Workplace conflict often starts small and grows costly when left alone. Clear expectations, early action and respectful conversations help teams stay productive, engaged and safe while reducing legal risk for everyone involved.</p>
    <p>Managers need practical tools to recognise problem behaviour, respond with confidence and keep decisions fair, consistent and well documented across the whole organisation.</p>
    <p>Workplace conflict often starts small and grows costly when left alone. Clear expectations, early action and respectful conversations help teams stay productive, engaged and safe while reducing legal risk for everyone involved.</p>
    <h3>LEARNING OUTCOMES</h3>
    <p class="lead">Training utilises learnings from recent case law, case studies, &amp; activities to apply the tools taught, to enable HR to assist managers to:</p>
    <ol>
      <li>Understand the legal framework that applies to workplace behaviour.</li>
      <li>Recognise early signs of conflict and act before issues escalate.</li>
      <li>Apply a simple, fair process to complaints and concerns.</li>
      <li>Hold respectful conversations that build trust and accountability.</li>
    </ol>
  </aside>
  <section class="main">
    <h2 class="title"><span class="lead-line" style="font-size:18px">MANAGING CONFLICT</span><span class="tail-line" style="font-size:11.5px">&amp; COMPLAINTS (CONDUCT)</span></h2>
    <div class="overview-head">OVERVIEW <span>OF</span> TRAINING</div>
    <div class="overview">
      <div class="topic"><div class="topic-name">Understanding how we label workplace conflict and the relevant legal framework</div><ul class="topic-points"><li>What it means in practice, why it matters and how to respond well.</li><li>Practical examples, common mistakes and simple steps managers can take.</li></ul></div>
      <div class="topic"><div class="topic-name">How to identify common causes of conflict &amp; problems with the common approach to resolution</div><ul class="topic-points"><li>What it means in practice, why it matters and how to respond well.</li><li>Practical examples, common mistakes and simple steps managers can take.</li></ul></div>
      <div class="topic"><div class="topic-name">3 Step approach to dealing with workplace conflict and complaints: Assess Risk, Determine Facts and Decide Outcomes</div><ul class="topic-points"><li>What it means in practice, why it matters and how to respond well.</li><li>Practical examples, common mistakes and simple steps managers can take.</li></ul></div>
      <div class="topic"><div class="topic-name">Using a Response Action Plan to implement the 3 Step approach</div><ul class="topic-points"><li>What it means in practice, why it matters and how to respond well.</li><li>Practical examples, common mistakes and simple steps managers can take.</li></ul></div>
      <div class="topic"><div class="topic-name">Examples of scenarios</div><ul class="topic-points"><li>What it means in practice, why it matters and how to respond well.</li><li>Practical examples, common mistakes and simple steps managers can take.</li></ul></div>
    </div>
  </section>
  <footer class="contact"><span>12 Harbour Lane, Northgate<br>Level 3, 80 Quay St, Southbank</span><span>1300 555 019</span><span>info@brindlelegal.com.au<br>www.brindlelegal.com.au</span><span class="social"><i class="dot"></i><i class="dot"></i></span></footer>
</article>

</body>
</html>
```